Marrowby Therapy and Consulting

Build & publish a WordPress website that advertises and markets my private practice - which is delivering, and consulting in, psychological therapies. I also need to be able to edit content (eg text and images) on the end product thereafter. It should have a call to action on the homepage, links to:
• About me
• For referrers (with link to service fees)
• Contact details – phone#, email address, location, operating hours, and service fees
• Other resources

Target Market(s)

People struggling with mental health, relationships, and/or psychological disorders

Industry/Entity Type

Mental health

Coding

Coded - Design and coding required

Number of Pages Required

4 page

Requirements
Must have
• WordPress
Nice to have
• Please make my logo standout on the home page
Should not have
• No testimonials - they're forbidden for psychologists in Australia

```html
<!DOCTYPE html>
<html lang="en">
<head>
<meta charset="utf-8">
<title>Marrowby Therapy and Consulting – Website Design</title>
<link href="https://fonts.googleapis.com/css2?family=Libre+Baskerville:wght@400;700&family=Manrope:wght@400;500;600;700&display=swap" rel="stylesheet">
<style>
:root{
  --board:#f8e4fa;
  --white:#ffffff;
  --ink:#161616;
  --muted:#555a60;
  --pink:#d79be0;
  --pink-deep:#c77fd4;
  --cyan:#3cc8e0;
  --cyan-soft:#c6eef5;
  --card:#f0f9fb;
  --teal:#0f8ea0;
  --footer:#1b1b1b;
}
*{box-sizing:border-box;margin:0;padding:0}
html,body{width:1200px;height:1200px;overflow:hidden}
body{background:var(--board);font-family:"Manrope",sans-serif;color:var(--ink);position:relative}
.abs{position:absolute}
.serif{font-family:"Libre Baskerville",serif;font-weight:700;letter-spacing:.02em}

/* board header */
.board-kicker{left:150px;top:13px;font-size:6px;font-weight:700;font-family:"Libre Baskerville",serif}
.board-title{left:150px;top:26px;font-size:13px}
.board-sub{left:150px;top:45px;font-size:7px;line-height:10px;color:#444;width:160px}

/* left page */
.page-left{left:152px;top:87px;width:393px;height:1113px;background:var(--white);overflow:hidden}
.nav{position:absolute;left:0;top:0;width:100%;height:23px;display:flex;align-items:center}
.brand{position:absolute;left:63px;top:6px;display:flex;align-items:center;gap:3px;font-size:5.5px;color:#556;font-weight:500}
.brand-dot{width:9px;height:9px;border-radius:50%;border:1px solid var(--cyan)}
.nav-links{position:absolute;left:183px;top:9px;display:flex;gap:7px;font-size:4.2px;color:#777}
.nav-links .on{color:var(--pink-deep);font-weight:600}
.nav-cta{position:absolute;left:288px;top:5px;width:44px;height:14px;background:var(--pink);color:#fff;font-size:5px;display:flex;align-items:center;justify-content:center;border-radius:1px}
.hero{position:absolute;left:0;top:23px;width:393px;height:225px;background:linear-gradient(100deg,#f2ece8 0%,#e8dcd6 40%,#d9c2bc 70%,#c8a9b8 100%)}
.hero-glow{position:absolute;left:230px;top:0;width:163px;height:90px;background:radial-gradient(ellipse at 40% 40%,rgba(228,150,240,.8),rgba(200,170,250,.2) 60%,transparent 75%)}
.social-rail{position:absolute;left:0;top:16px;width:19px;height:168px;background:#1e1e22;color:#fff;font-size:4px;writing-mode:vertical-rl;display:flex;align-items:center;justify-content:center;gap:6px;letter-spacing:.03em}
.hero h1{position:absolute;left:61px;top:32px;font-size:18px;font-family:"Libre Baskerville",serif;font-weight:700}
.hero-sub{position:absolute;left:61px;top:60px;font-size:7px;color:#333}
.hero-btn{position:absolute;left:61px;top:75px;width:114px;height:19px;background:var(--pink);color:#fff;font-size:6px;display:flex;align-items:center;padding-left:11px;gap:8px}
.slider{position:absolute;left:258px;top:205px;display:flex;gap:3px}
.slider i{display:block;width:16px;height:3px;background:var(--pink)}
.slider i.cur{background:#fff}
.slider-num{position:absolute;left:301px;top:197px;font-size:5px}

.meet-photo{position:absolute;left:61px;top:308px;width:109px;height:126px;border-radius:55px 55px 0 0;background:linear-gradient(180deg,#6f8a6a,#4c5e49 55%,#3d5470);box-shadow:0 0 14px 4px rgba(60,200,224,.55)}
.meet{position:absolute;left:194px;top:297px;width:135px}
.meet-kicker{font-size:5.5px;font-family:"Libre Baskerville",serif;text-decoration:underline;color:#555}
.meet h2{font-size:12.5px;margin-top:12px}
.meet-role{color:var(--cyan);font-size:6.5px;line-height:10px;margin-top:4px}
.meet p{font-size:4.6px;line-height:11.5px;color:#444;margin-top:6px}
.meet-btn{margin-top:10px;width:72px;height:14px;background:var(--pink);color:#fff;font-size:4.7px;display:flex;align-items:center;justify-content:center}

.services{position:absolute;left:0;top:521px;width:393px;height:198px;background:var(--cyan);color:#fff}
.services h2{position:absolute;left:0;right:0;top:16px;text-align:center;font-size:12px}
.svc{position:absolute;width:84px;text-align:center;font-size:6.5px;font-weight:600;border-bottom:1px solid rgba(255,255,255,.7);padding-bottom:4px}
.svc svg{display:block;margin:0 auto 7px}
.svc-btn{position:absolute;left:210px;top:175px;width:122px;height:23px;background:var(--pink);display:flex;align-items:center;justify-content:center;gap:10px;font-size:6.3px;font-weight:500}

.sec-title{position:absolute;text-align:center;font-size:10.5px}
.grid{position:absolute;display:grid;grid-template-columns:repeat(3,85px);column-gap:8px;row-gap:8px}
.card{height:105px;background:var(--card)}
.card .art{height:47px}
.card h3{font-family:"Libre Baskerville",serif;font-size:6px;font-weight:700;letter-spacing:.02em;line-height:9.5px;padding:5px 4px 0}
.card p{font-size:4.2px;line-height:8.2px;color:#333;padding:3px 4px 0}
.card.hl{background:var(--cyan)}
.card.hl h3,.card.hl p{color:#fff}

/* right page */
.page-right{left:612px;top:0;width:393px;height:1200px;background:var(--white);overflow:hidden}
.load-btn{position:absolute;left:172px;top:384px;width:49px;height:14px;background:var(--pink);color:#fff;font-size:4.6px;display:flex;align-items:center;justify-content:center}
.approach{position:absolute;left:0;top:443px;width:393px;height:125px;background:var(--cyan-soft)}
.approach h2{position:absolute;left:0;right:0;top:18px;text-align:center;font-size:10.5px}
.ap{position:absolute;display:flex;align-items:center;gap:4px;font-size:6.5px;font-weight:600}
.ap .ic{width:25px;height:25px;border-radius:50%;background:var(--cyan);border:1.5px solid var(--pink);display:flex;align-items:center;justify-content:center}
.ap span{border-bottom:1px solid #8fbfc8;padding:0 3px 3px}

.video h2{position:absolute;left:62px;top:597px;font-size:10.5px}
.video p{position:absolute;left:62px;top:618px;width:205px;font-size:4.4px;line-height:8.3px;color:#333}
.video-btn{position:absolute;left:62px;top:651px;width:76px;height:15px;border:1px solid var(--pink);color:var(--pink-deep);font-size:4.6px;display:flex;align-items:center;justify-content:center;gap:6px}
.ph{position:absolute;width:131px;height:89px}
.tag{position:absolute;right:5px;top:5px;background:var(--pink);color:#fff;font-size:4.4px;padding:2px 4px}

.newclient{position:absolute;left:0;top:912px;width:393px;height:63px;background:var(--cyan-soft)}
.newclient h2{text-align:center;font-size:10.5px;line-height:16.5px;margin-top:15px}
.loc{position:absolute;left:0;top:975px;width:172px;height:125px;background:var(--teal);color:#fff}
.loc h2{position:absolute;left:10px;top:22px;font-size:10.5px;word-spacing:3px}
.loc-addr{position:absolute;left:10px;top:38px;width:162px;height:22px;background:var(--pink);font-size:4.5px;line-height:11px;padding-left:15px}
.loc-row{position:absolute;left:12px;display:flex;align-items:center;gap:6px;font-size:6.5px}
.map{position:absolute;left:172px;top:975px;width:221px;height:125px;background:linear-gradient(160deg,#eef1f2,#dfe4e6)}
.foot{position:absolute;left:0;top:1100px;width:393px;height:100px;background:var(--footer);color:#fff}
.foot-brand{position:absolute;left:0;right:0;top:24px;display:flex;justify-content:center;align-items:center;gap:3px;font-size:6px}
.foot-links{position:absolute;left:0;right:0;top:44px;display:flex;justify-content:center;gap:9px;font-size:4.5px}
.foot-rule{position:absolute;left:61px;right:61px;top:72px;height:1px;background:#555}
.foot-copy{position:absolute;left:61px;top:78px;font-size:3.4px;color:#ccc}
.foot-legal{position:absolute;right:61px;top:78px;display:flex;gap:6px;font-size:3.4px;color:#ccc;text-decoration:underline}
</style>
</head>
<body>

<div class="abs board-kicker">WEBSITE FOR</div>
<div class="abs board-title serif">MR DECLAN HART</div>
<div class="abs board-sub">CLINICAL PSYCHOLOGIST, CLINICAL SUPERVISOR</div>

<!-- Left page -->
<section class="abs page-left">
  <header class="nav">
    <div class="brand"><span class="brand-dot"></span>Marrowby</div>
    <nav class="nav-links"><span class="on">Home</span><span>About Me</span><span>For Referrers</span><span>Contact</span></nav>
    <div class="nav-cta">Get a Quote</div>
  </header>

  <div class="hero" role="img" aria-label="Photo of a relaxed woman resting her head with a soft glowing light">
    <div class="hero-glow"></div>
    <div class="social-rail">CIRCLEBOOK · PICTORIA · CHIRP · WORKLINE · VIEWTUBE</div>
    <h1>HEALING MINDS</h1>
    <div class="hero-sub">MARROWBY THERAPY AND CONSULTING</div>
    <div class="hero-btn">BOOK AN APPOINTMENT
      <svg width="8" height="7" viewBox="0 0 8 7" fill="none" stroke="#fff" stroke-width=".7"><rect x=".5" y=".5" width="7" height="6"/><path d="M2 3h4M2 5h3"/></svg>
    </div>
    <div class="slider-num">03</div>
    <div class="slider"><i></i><i></i><i class="cur"></i><i></i></div>
  </div>

  <div class="meet-photo" role="img" aria-label="Portrait photo of Mr Declan Hart"></div>
  <div class="meet">
    <div class="meet-kicker">MEET</div>
    <h2 class="serif">MR DECLAN HART</h2>
    <div class="meet-role">CLINICAL PSYCHOLOGIST, CLINICAL SUPERVISOR</div>
    <p>I'm a clinical psychologist, psychotherapist, EMDR Consultant, and Resource Therapy Practitioner and Trainer. My main interest in therapy is helping people overcome the inner obstacles that cause them emotional pain and suffering, and that maintain behavioural patterns that are damaging or self-defeating. I also like to train, coach and mentor other therapists in effective therapies.</p>
    <div class="meet-btn">LEARN MORE ABOUT</div>
  </div>

  <section class="services">
    <h2 class="serif">SERVICES WE OFFER</h2>
    <div class="svc" style="left:61px;top:46px">
      <svg width="14" height="15" viewBox="0 0 14 15" fill="none" stroke="#fff" stroke-width="1"><path d="M3 14v-3C1 9.5 1 6 2.5 4 4 1.5 8 1 10.5 3c2 1.7 2 4.5 1 6L13 11h-1.5v3"/><circle cx="7" cy="6" r="1.5"/></svg>Psychotherapy</div>
    <div class="svc" style="left:153px;top:46px">
      <svg width="14" height="14" viewBox="0 0 14 14" fill="none" stroke="#fff" stroke-width="1"><rect x="1" y="1" width="12" height="12" rx="1"/><path d="M4.5 10V7M7 10V4M9.5 10V6"/></svg>Assessment</div>
    <div class="svc" style="left:250px;top:82px;line-height:9px">
      <svg width="15" height="12" viewBox="0 0 15 12" fill="none" stroke="#fff" stroke-width="1"><rect x="1" y="1" width="13" height="9"/><path d="M6 3.5v4l3-2z M1 11.5h13"/></svg>Online Video<br>Consultations</div>
    <div class="svc" style="left:61px;top:105px">
      <svg width="16" height="15" viewBox="0 0 16 15" fill="none" stroke="#fff" stroke-width="1"><path d="M9 12H1V1h12v5"/><circle cx="12" cy="9" r="2"/><path d="M9 14c0-2 1.5-3 3-3s3 1 3 3M3 4l4 4"/></svg>Professional Training</div>
    <div class="svc" style="left:153px;top:105px">
      <svg width="14" height="15" viewBox="0 0 14 15" fill="none" stroke="#fff" stroke-width="1"><path d="M10 6V1H1v13h6"/><path d="M3 4h5M3 7h4"/><circle cx="10" cy="9" r="1.8"/><path d="M7 14c0-2 1.3-3 3-3s3 1 3 3"/></svg>Clinical Supervision</div>
    <div class="svc-btn">EXPLORE MORE SERVICES
      <svg width="6" height="6" viewBox="0 0 6 6" fill="none" stroke="#fff" stroke-width=".8"><path d="M5 5L1 1M1 4V1h3"/></svg>
    </div>
  </section>

  <h2 class="sec-title serif" style="left:0;right:0;top:767px">AREAS OF SPECIAL INTEREST</h2>
  <div class="grid" style="left:61px;top:795px">
    <div class="card hl"><div class="art" role="img" aria-label="Illustration of a person in therapy on a sofa" style="background:linear-gradient(135deg,#e9f7ee,#9fe0b8)"></div><h3>ADDICTION</h3><p>Lorem Ipsum Dolor Sit Amet Consectetur. Fermentum Ut Lobortis Ante Ac Risus Hendrerit. Diam Tincidunt Adipiscing Platea</p></div>
    <div class="card"><div class="art" role="img" aria-label="Illustration of an angry group of people" style="background:linear-gradient(135deg,#3050c8,#f0b020)"></div><h3>ANGER RELATED ISSUES</h3><p>Lorem Ipsum Dolor Sit Amet Consectetur. Fermentum Ut Lobortis Ante Ac Risus Hendrerit.</p></div>
    <div class="card"><div class="art" role="img" aria-label="Illustration of an anxious person holding their head" style="background:linear-gradient(135deg,#f4eefa,#6a4a8a)"></div><h3>ANXIETY / PANIC ATTACKS</h3><p>Lorem Ipsum Dolor Sit Amet Consectetur. Fermentum Ut Lobortis Ante Ac Risus Hendrerit.</p></div>
    <div class="card"><div class="art" role="img" aria-label="Illustration of confident people standing" style="background:linear-gradient(135deg,#fbdede,#e88a7a)"></div><h3>ASSERTIVENESS</h3><p>Lorem Ipsum Dolor Sit Amet Consectetur. Fermentum Ut Lobortis Ante Ac Risus Hendrerit. Diam Tincidunt Adipiscing Platea</p></div>
    <div class="card"><div class="art" role="img" aria-label="Illustration of a crowd with speech bubbles" style="background:linear-gradient(135deg,#e8eef0,#3c5a62)"></div><h3>BORDERLINE PERSONALITY</h3><p>Lorem Ipsum Dolor Sit Amet Consectetur. Fermentum Ut Lobortis Ante Ac Risus Hendrerit.</p></div>
    <div class="card"><div class="art" role="img" aria-label="Illustration of a sad person in distress" style="background:linear-gradient(135deg,#fde4ea,#4a7ab0)"></div><h3>DEPRESSION</h3><p>Lorem Ipsum Dolor Sit Amet Consectetur. Fermentum Ut Lobortis Ante Ac Risus Hendrerit. Diam Tincidunt Adipiscing Platea</p></div>
    <div class="card"><div class="art" role="img" aria-label="Illustration of a person sitting alone at night" style="background:linear-gradient(135deg,#1a2a50,#3a5aa0)"></div><h3>DISSOCIATIVE DISORDERS</h3><p>Lorem Ipsum Dolor Sit Amet Consectetur. Fermentum Ut Lobortis Ante Ac Risus Hendrerit.</p></div>
    <div class="card"><div class="art" role="img" aria-label="Illustration of a doctor with a patient" style="background:linear-gradient(135deg,#f3f5f8,#e07a7a)"></div><h3>DUAL DIAGNOSIS</h3><p>Lorem Ipsum Dolor Sit Amet Consectetur. Fermentum Ut Lobortis Ante Ac Risus Hendrerit. Diam Tincidunt Adipiscing Platea</p></div>
    <div class="card"><div class="art" role="img" aria-label="Illustration of a person surrounded by thoughts" style="background:linear-gradient(135deg,#eeeeee,#f2c830)"></div><h3>EXISTENTIAL ISSUES</h3><p>Lorem Ipsum Dolor Sit Amet Consectetur. Fermentum Ut Lobortis Ante Ac Risus Hendrerit. Diam Tincidunt Adipiscing Platea</p></div>
  </div>
</section>

<!-- Right page -->
<section class="abs page-right">
  <h2 class="sec-title serif" style="left:0;right:0;top:12px">AREAS OF SPECIAL INTEREST</h2>
  <div class="grid" style="left:61px;top:39px;row-gap:8px">
    <div class="card hl" style="height:105px"><div class="art" role="img" aria-label="Illustration of a person in therapy on a sofa" style="background:linear-gradient(135deg,#e9f7ee,#9fe0b8)"></div><h3>ADDICTION</h3><p>Lorem Ipsum Dolor Sit Amet Consectetur. Fermentum Ut Lobortis Ante Ac Risus Hendrerit. Diam Tincidunt Adipiscing Platea</p></div>
    <div class="card"><div class="art" role="img" aria-label="Illustration of an angry group of people" style="background:linear-gradient(135deg,#3050c8,#f0b020)"></div><h3>ANGER RELATED ISSUES</h3><p>Lorem Ipsum Dolor Sit Amet Consectetur. Fermentum Ut Lobortis Ante Ac Risus Hendrerit.</p></div>
    <div class="card"><div class="art" role="img" aria-label="Illustration of an anxious person holding their head" style="background:linear-gradient(135deg,#f4eefa,#6a4a8a)"></div><h3>ANXIETY / PANIC ATTACKS</h3><p>Lorem Ipsum Dolor Sit Amet Consectetur. Fermentum Ut Lobortis Ante Ac Risus Hendrerit.</p></div>
    <div class="card"><div class="art" role="img" aria-label="Illustration of confident people standing" style="background:linear-gradient(135deg,#fbdede,#e88a7a)"></div><h3>ASSERTIVENESS</h3><p>Lorem Ipsum Dolor Sit Amet Consectetur. Fermentum Ut Lobortis Ante Ac Risus Hendrerit. Diam Tincidunt Adipiscing Platea</p></div>
    <div class="card"><div class="art" role="img" aria-label="Illustration of a crowd with speech bubbles" style="background:linear-gradient(135deg,#e8eef0,#3c5a62)"></div><h3>BORDERLINE PERSONALITY</h3><p>Lorem Ipsum Dolor Sit Amet Consectetur. Fermentum Ut Lobortis Ante Ac Risus Hendrerit.</p></div>
    <div class="card"><div class="art" role="img" aria-label="Illustration of a sad person in distress" style="background:linear-gradient(135deg,#fde4ea,#4a7ab0)"></div><h3>DEPRESSION</h3><p>Lorem Ipsum Dolor Sit Amet Consectetur. Fermentum Ut Lobortis Ante Ac Risus Hendrerit. Diam Tincidunt Adipiscing Platea</p></div>
    <div class="card"><div class="art" role="img" aria-label="Illustration of a person sitting alone at night" style="background:linear-gradient(135deg,#1a2a50,#3a5aa0)"></div><h3>DISSOCIATIVE DISORDERS</h3><p>Lorem Ipsum Dolor Sit Amet Consectetur. Fermentum Ut Lobortis Ante Ac Risus Hendrerit.</p></div>
    <div class="card"><div class="art" role="img" aria-label="Illustration of a doctor with a patient" style="background:linear-gradient(135deg,#f3f5f8,#e07a7a)"></div><h3>DUAL DIAGNOSIS</h3><p>Lorem Ipsum Dolor Sit Amet Consectetur. Fermentum Ut Lobortis Ante Ac Risus Hendrerit. Diam Tincidunt Adipiscing Platea</p></div>
    <div class="card"><div class="art" role="img" aria-label="Illustration of a person surrounded by thoughts" style="background:linear-gradient(135deg,#eeeeee,#f2c830)"></div><h3>EXISTENTIAL ISSUES</h3><p>Lorem Ipsum Dolor Sit Amet Consectetur. Fermentum Ut Lobortis Ante Ac Risus Hendrerit. Diam Tincidunt Adipiscing Platea</p></div>
  </div>
  <div class="load-btn">LOAD MORE</div>

  <section class="approach">
    <h2 class="serif">APPROACH</h2>
    <div class="ap" style="left:24px;top:45px"><span class="ic"><svg width="11" height="11" viewBox="0 0 11 11" fill="none" stroke="#fff" stroke-width=".8"><circle cx="4" cy="3" r="2"/><path d="M1 9c0-2.5 1.5-3.5 3-3.5s3 1 3 3.5M7 6l3 3"/></svg></span><span>EMDR</span></div>
    <div class="ap" style="left:89px;top:45px"><span class="ic"><svg width="11" height="11" viewBox="0 0 11 11" fill="none" stroke="#fff" stroke-width=".8"><circle cx="4" cy="3" r="2"/><path d="M1 9c0-2.5 1.5-3.5 3-3.5s3 1 3 3.5M7 6l3 3"/></svg></span><span>INTEGRATIVE</span></div>
    <div class="ap" style="left:178px;top:45px"><span class="ic"><svg width="11" height="11" viewBox="0 0 11 11" fill="none" stroke="#fff" stroke-width=".8"><circle cx="4" cy="3" r="2"/><path d="M1 9c0-2.5 1.5-3.5 3-3.5s3 1 3 3.5M7 6l3 3"/></svg></span><span>MINDFULNESS</span></div>
    <div class="ap" style="left:271px;top:45px"><span class="ic"><svg width="11" height="11" viewBox="0 0 11 11" fill="none" stroke="#fff" stroke-width=".8"><circle cx="4" cy="3" r="2"/><path d="M1 9c0-2.5 1.5-3.5 3-3.5s3 1 3 3.5M7 6l3 3"/></svg></span><span>PERSON CENTRED</span></div>
    <div class="ap" style="left:66px;top:78px"><span class="ic"><svg width="11" height="11" viewBox="0 0 11 11" fill="none" stroke="#fff" stroke-width=".8"><circle cx="4" cy="3" r="2"/><path d="M1 9c0-2.5 1.5-3.5 3-3.5s3 1 3 3.5M7 6l3 3"/></svg></span><span>PSYCHODYNAMIC</span></div>
    <div class="ap" style="left:171px;top:78px"><span class="ic"><svg width="11" height="11" viewBox="0 0 11 11" fill="none" stroke="#fff" stroke-width=".8"><circle cx="4" cy="3" r="2"/><path d="M1 9c0-2.5 1.5-3.5 3-3.5s3 1 3 3.5M7 6l3 3"/></svg></span><span>SCHEMA THERAPY</span></div>
    <div class="ap" style="left:277px;top:78px"><span class="ic"><svg width="11" height="11" viewBox="0 0 11 11" fill="none" stroke="#fff" stroke-width=".8"><circle cx="4" cy="3" r="2"/><path d="M1 9c0-2.5 1.5-3.5 3-3.5s3 1 3 3.5M7 6l3 3"/></svg></span><span>CBT</span></div>
  </section>

  <section class="video">
    <h2 class="serif">CONVENIENT VIDEO CONFERENCING</h2>
    <p>Lorem Ipsum Dolor Sit Amet Consectetur. Fermentum Ut Lobortis Ante Ac Risus Hendrerit. Diam Tincidunt Adipiscing Platea &nbsp;Fermentum Ut Lobortis Ante Ac Risus Hendrerit. Diam Tincidunt Adipiscing Platea</p>
    <div class="video-btn">ONLINE THERAPY
      <svg width="5" height="5" viewBox="0 0 6 6" fill="none" stroke="#c77fd4" stroke-width=".8"><path d="M5 5L1 1M1 4V1h3"/></svg>
    </div>
    <div class="ph" role="img" aria-label="Photo of a group of smiling teenagers at a playground" style="left:62px;top:682px;background:linear-gradient(135deg,#8aa0b8,#4a4a5a 60%,#c8a060)"><span class="tag">TEEN</span></div>
    <div class="ph" role="img" aria-label="Photo of a smiling woman in a red top pointing" style="left:201px;top:682px;background:linear-gradient(135deg,#f4f4f4,#e8e4e2 55%,#d24a3a)"><span class="tag">WOMEN</span></div>
    <div class="ph" role="img" aria-label="Photo of a happy child in a striped jumper giving thumbs up" style="left:62px;top:779px;background:linear-gradient(135deg,#dcd8d4,#c8c0b8 50%,#7a9ab8)"><span class="tag">CHILD</span></div>
    <div class="ph" role="img" aria-label="Photo of a family walking together in a park" style="left:201px;top:779px;background:linear-gradient(135deg,#5a7a3a,#8aa860 50%,#6a8a9a)"><span class="tag">PARENT AND FAMILY</span></div>
  </section>

  <section class="newclient">
    <h2 class="serif">NEW CLIENT? LEARN MORE ABOUT<br>GETTING STARTED</h2>
  </section>

  <section class="loc">
    <h2 class="serif">PRACTICE LOCATION</h2>
    <div class="loc-addr">SUITE 4, FERRIS HOUSE, 12 FERRIS STREET,<br>MARROWBY, TAS 7000</div>
    <div class="loc-row" style="top:66px"><svg width="9" height="7" viewBox="0 0 9 7" fill="none" stroke="#fff" stroke-width=".7"><rect x=".5" y=".5" width="8" height="6"/><path d="M.5 .5l4 3.5 4-3.5"/></svg>declan.hart@marrowbymail.au</div>
    <div class="loc-row" style="top:82px"><svg width="8" height="8" viewBox="0 0 8 8" fill="none" stroke="#fff" stroke-width=".7"><path d="M1.5 .8l1.3 1.8-.8 1c.5 1 1.3 1.8 2.3 2.3l1-.8 1.8 1.3-.8 1.2C3.5 7.4.6 4.5.3 1.6z"/></svg>0400 555 019</div>
  </section>
  <div class="map" role="img" aria-label="Map of Australia and New Zealand with a pin marking the practice"></div>

  <footer class="foot">
    <div class="foot-brand"><span class="brand-dot"></span>Marrowby</div>
    <nav class="foot-links"><span>Home</span><span>About Me</span><span>For Referrers</span><span>Contact</span><span>Blog</span></nav>
    <div class="foot-rule"></div>
    <div class="foot-copy">© 2023 Marrowby. All rights reserved.</div>
    <div class="foot-legal"><span>Privacy Policy</span><span>Terms of Service</span><span>Cookies Settings</span></div>
  </footer>
</section>

</body>
</html>
```